Pawn & Gun store business card design

Hello! We would like a new business card design for our pawn & gun store. We loan money on items of value and sell firearms, jewelry, electronics & more.

Card will need to have the following information:

Business name - Prairie Mint Pawn & Gun
Address - 2417 Cedar Bend Rd. Suite B Wylie, TX 75098
Employees name - Carl Hembree
Phone number - 972-555-0183
Email - PrairieMintPawn@Mailvex.com
Website - PrairieMintPawn.com

Somewhere on the card we would like it to say "Offering 10 Month Layaway!" & "We buy & loan on anything of value!". Our main store color is orange (please see logo). Logo does not have to be on the business card but it can be. Would like the back to have an area to write a note on the back. We like vintage things like old coins, collectables, firearms and more so think about this in the design. We want a business card as unique as our store!

Colors

Designer to choose colors to be used in the design.

Requirements
Nice to have
• Vintage Style

```html
<!DOCTYPE html>
<html lang="en">
<head>
<meta charset="utf-8">
<title>Prairie Mint Pawn &amp; Gun — Business Card</title>
<link rel="stylesheet" href="https://fonts.googleapis.com/css2?family=Oswald:wght@300;400;500;600&display=swap">
<style>
  :root {
    --bg: #9b9b9b;
    --paper: #f7f6f2;
    --ink: #3a2417;
    --orange: #e3682b;
    --rule: #5a4030;
  }
  * { box-sizing: border-box; margin: 0; padding: 0; }
  html, body {
    width: 1200px; height: 1059px; overflow: hidden;
    background: var(--bg);
    font-family: "Oswald", "Arial Narrow", sans-serif;
    color: var(--ink);
  }
  .stage {
    width: 1200px; height: 1059px;
    display: flex; align-items: center; justify-content: center; gap: 56px;
  }
  .card {
    position: relative;
    background: var(--paper);
    box-shadow: 0 3px 0 var(--orange), 0 14px 30px rgba(0,0,0,.25);
  }
  .card-front { width: 380px; height: 665px; }
  .card-back  { width: 665px; height: 380px; }

  .frame {
    position: absolute; inset: 16px;
    border: 2px solid var(--ink);
  }

  /* Front */
  .front-body {
    position: absolute; inset: 18px;
    display: flex; flex-direction: column; align-items: center;
    padding: 0 24px;
  }
  .brand {
    flex: none; height: 205px; width: 100%;
    display: flex; align-items: center; justify-content: center; gap: 12px;
  }
  .brand-dot {
    width: 22px; height: 22px; border-radius: 50%;
    background: var(--orange); flex: none;
  }
  .brand-name {
    font-weight: 600; font-size: 32px; line-height: 1.05;
    color: var(--orange); text-transform: uppercase; letter-spacing: .5px;
  }
  .divider { flex: none; width: 100%; height: 0; border-top: 2px solid var(--rule); }
  .section {
    flex: none; width: 100%; text-align: center; text-transform: uppercase;
    display: flex; flex-direction: column; justify-content: center;
    white-space: nowrap; overflow: hidden;
  }
  .person-name {
    height: 92px;
    font-weight: 500; font-size: 40px; line-height: 1; color: var(--orange); letter-spacing: 1px;
  }
  .store { height: 88px; }
  .store-name { font-weight: 500; font-size: 22px; line-height: 1.15; }
  .store-address { font-weight: 300; font-size: 13.5px; line-height: 1.35; }
  .contact { height: 100px; }
  .phone { font-weight: 400; font-size: 44px; line-height: 1.05; letter-spacing: 1px; }
  .email { font-weight: 300; font-size: 15px; line-height: 1.25; }
  .web { height: 86px; font-weight: 600; font-size: 20px; letter-spacing: .5px; }

  /* Back */
  .back-frame {
    position: absolute; inset: 16px;
    border: 2px solid var(--ink);
  }
  .note-lines {
    position: absolute; left: 52px; right: 52px; top: 48px;
    display: flex; flex-direction: column; gap: 36px;
  }
  .note-lines span { display: block; border-top: 1px solid var(--rule); }
  .offer {
    position: absolute; left: 0; right: 0; top: 212px;
    text-align: center; text-transform: uppercase; line-height: 1.2;
  }
  .offer-layaway { color: var(--orange); font-weight: 500; font-size: 20px; letter-spacing: .5px; }
  .offer-buy { font-weight: 400; font-size: 17px; }
  .pistols {
    position: absolute; left: 50%; bottom: 22px; transform: translateX(-50%);
    width: 170px; height: 58px; border-radius: 8px;
    background: linear-gradient(180deg, #5a3a26, #3a2417);
  }
  .flourish {
    position: absolute; bottom: 30px; width: 80px; height: 16px; border-radius: 8px;
    background: linear-gradient(90deg, rgba(58,36,23,.15), rgba(58,36,23,.45), rgba(58,36,23,.15));
  }
  .flourish-left { left: 30px; }
  .flourish-right { right: 30px; }
</style>
</head>
<body>
<main class="stage">
  <section class="card card-front" aria-label="Card front">
    <div class="frame"></div>
    <div class="front-body">
      <div class="brand">
        <span class="brand-dot"></span>
        <span class="brand-name">Prairie Mint Pawn</span>
      </div>
      <div class="divider"></div>
      <div class="section person-name">Carl Hembree</div>
      <div class="divider"></div>
      <div class="section store">
        <div class="store-name">Prairie Mint Pawn &amp; Gun</div>
        <div class="store-address">2417 Cedar Bend Rd. Suite B Wylie, TX 75098</div>
      </div>
      <div class="divider"></div>
      <div class="section contact">
        <div class="phone">972-555-0183</div>
        <div class="email">PrairieMintPawn@Mailvex.com</div>
      </div>
      <div class="divider"></div>
      <div class="section web">www.PrairieMintPawn.com</div>
    </div>
  </section>

  <section class="card card-back" aria-label="Card back">
    <div class="back-frame"></div>
    <div class="note-lines"><span></span><span></span><span></span><span></span></div>
    <div class="offer">
      <div class="offer-layaway">Offering 10 Month Layaway</div>
      <div class="offer-buy">We buy &amp; loan on anything of value</div>
    </div>
    <div class="flourish flourish-left" role="img" aria-label="Vintage scroll flourish ornament"></div>
    <div class="flourish flourish-right" role="img" aria-label="Vintage scroll flourish ornament"></div>
    <div class="pistols" role="img" aria-label="Illustration of two crossed revolvers"></div>
  </section>
</main>
</body>
</html>
```